Web Site Design For Real Estate Sales Project

The idea behind this project is pretty simple. I am putting my penthouse apartment up for sale and am trying to be creative in selling it.
Technically this will be pretty simple, it will be 3 pages but graphically this has to be as impressive as possible which is why I am trying Pixel Harbor.
The apartment is located in Barra Da Tijuca, Rio De Janeiro, Brazil. (This is where the 2016 Meridian Regatta will be held)
I am looking for an index page and 2 sub-pages. I am open to all kinds of designs and navigation's but it has to make an impression quickly with a professional and enticing design. The index page should make it obvious that there is a penthouse apartment for sale in Barra Da Tijuca ( suburb of Rio De Janeiro). The first sub page is about the Condominium where the apartment is located, the second sub page is about the apartment itself.
Here is a more detailed description of what the 3 pages should be about.
Index Page
This is the landing page and should make it obvious that there is an apartment for sale in Barra Da Tijuca, Rio De Janeiro with the following attributes
251 SQ M
Duplex Penthouse
4 suites
Price R$ 2.200.000
Price per SQ M: R$ 8.764
First Sub-Page
This is about the Condominium which is called "Gentle Palm Residences" with the following bullets
*Family friendly and safe
*Direct access to the beach
*Many amenities like pool, football court, gym, sauna
There should be some photos of the condominium and a link to the site of the condominium ( www.gprvx.com )
Second Sub-page
This is about the apartment. It should list in bullets the features of the apartment and then have a photo gallery of the view and various rooms. I have attached sample photos but will eventually have to use more photos.
Apartment Features
Price: R$ 2.220.000
251 m2 Duplex Penthouse
4 suites
maids room with bath
guest bathroom
living room
dinning room
Terrace with heated pool for year round use
Veranda
As mentioned above I am open to all designs and navigation so feel free to be creative. The important thing is catch peoples attention and get the message across in a few seconds, which is that there is an apartment for sale at this price with these features in this location. I will then use brightlist promoter and SEO to get people to the site.
Thanks
Target Market(s)
Men and Women from 30-60 years of age.
Industry/Entity Type
Apartment

```html
<!DOCTYPE html>
<html lang="en">
<head>
<meta charset="utf-8">
<title>Gentle Palm Residences</title>
<link href="https://fonts.googleapis.com/css2?family=Open+Sans:wght@400;600;700&family=Arimo:wght@400;700&display=swap" rel="stylesheet">
<style>
:root{
  --blue:#2b9de2;
  --blue-dark:#1479c9;
  --accent:#3a9fd8;
  --ink:#444;
  --muted:#999;
  --line:#dcdcdc;
  --panel:#f9f9f9;
  --green:#5aa51c;
  --footer-top:#4a4a4a;
  --footer-bottom:#111;
}
*{box-sizing:border-box;margin:0;padding:0}
html,body{width:1200px;height:1081px;overflow:hidden;background:#fff}
body{position:relative;font-family:"Open Sans",Arial,sans-serif;color:var(--ink)}
.abs{position:absolute}
.top-rule{left:0;top:0;width:1200px;height:4px;background:var(--blue-dark)}
.page-frame{left:41px;top:4px;width:1123px;height:997px;border:1px solid var(--line);border-top:none}
.utility{left:799px;top:4px;width:359px;height:30px;background:linear-gradient(var(--blue),var(--blue-dark));
  clip-path:polygon(0 0,100% 0,100% 100%,9% 100%);display:flex;justify-content:flex-end;align-items:center;padding-right:16px;
  font-size:13px;color:#fff;gap:13px}
.utility span.sep{opacity:.8}
.brand{left:48px;top:10px;font-family:"Arimo",Arial,sans-serif;font-weight:700;color:var(--ink);font-size:40px;line-height:46px;letter-spacing:.5px}
.social{left:974px;top:67px;display:flex;gap:8px}
.social i{display:block;width:30px;height:30px;border-radius:3px}
.nav{left:46px;top:108px;width:1112px;height:51px;background:linear-gradient(#3aa8ea,#1681d0);border-top:1px solid #7cc6f2}
.nav a{position:absolute;top:13px;color:#fff;font-size:17px;text-decoration:none}
.nav .sep{position:absolute;top:14px;width:1px;height:24px;background:#a6d6f4}
.search{position:absolute;left:793px;top:10px;width:260px;height:32px;background:#fff;border-radius:4px;font-size:12.5px;color:#888;padding:8px 15px;letter-spacing:.5px}
.go{position:absolute;left:1058px;top:10px;width:32px;height:32px;background:linear-gradient(#6dbb2a,#4b9212);border-radius:3px;font-size:13px;color:#222;text-align:center;line-height:32px}
.hero{left:46px;top:163px;width:1112px;height:408px;background:#ddd}
.hero-photo{position:absolute;left:5px;top:5px;width:1103px;height:398px;
  background:linear-gradient(180deg,#e9e6df 0%,#cfc7bb 35%,#6e4a32 62%,#3e2619 100%)}
.hero-caption{position:absolute;left:5px;top:306px;width:1103px;height:97px;background:rgba(20,14,10,.45)}
.hero-title{left:66px;top:477px;color:#fff;font-size:21px;font-weight:600}
.hero-text{left:64px;top:511px;width:540px;color:#fff;font-size:14px;line-height:17px}
.hero-price{left:900px;top:477px;width:232px;text-align:right;color:#fff;font-size:21px;font-weight:600}
.read-more{left:1042px;top:529px;width:90px;height:26px;border-radius:4px;background:linear-gradient(#49acf0,#1f86dc);color:#fff;font-size:14px;text-align:center;line-height:26px}
.arrow{top:322px;width:46px;height:46px;border-radius:50%;background:#fff}
.heading{font-size:26px;color:#555;letter-spacing:-.5px}
.heading b{color:var(--accent);font-weight:600}
.heading.small{font-size:21px}
.heading.small b{color:#555}
.underline{height:0;border-top:1px dashed #ddd}
.welcome-box{left:44px;top:642px;width:740px;height:102px;background:var(--panel);border:1px solid #ececec;padding:10px 9px;font-size:14.5px;line-height:18.5px;color:#555;letter-spacing:.3px}
.welcome-box .more{color:#2a7fc0;font-size:13px}
.photo{background:#888}
.features{left:803px;top:643px;width:353px;height:322px;border:1px solid var(--line);background:#fff}
.feature{position:absolute;left:10px;width:340px;height:90px}
.thumb{position:absolute;left:0;top:0;width:130px;height:87px;border:1px solid #ccc;padding:3px;background:#fff}
.thumb div{width:100%;height:100%}
.f-title{position:absolute;left:143px;top:1px;font-family:"Arimo",Arial,sans-serif;font-size:15px;font-weight:700;color:#333}
.f-addr{position:absolute;left:143px;top:28px;font-family:"Arimo",Arial,sans-serif;font-size:11px;color:var(--muted)}
.f-price{position:absolute;left:143px;top:51px;font-family:Georgia,serif;font-size:13px;font-weight:700;color:#555}
.f-specs{position:absolute;left:143px;top:73px;font-family:"Arimo",Arial,sans-serif;font-size:13px;color:#666}
.footer{left:0;top:1018px;width:1200px;height:63px;background:linear-gradient(var(--footer-top),var(--footer-bottom))}
.footer-links{position:absolute;left:45px;top:23px;font-family:"Arimo",Arial,sans-serif;font-size:12.5px;color:#fff;word-spacing:1px}
.copyright{position:absolute;right:40px;top:23px;font-family:"Arimo",Arial,sans-serif;font-size:12.5px;color:#fff}
</style>
</head>
<body>
<div class="abs top-rule"></div>
<div class="abs page-frame"></div>

<div class="abs utility">
  <span>Log-in</span><span class="sep">|</span><span>Brochures</span><span class="sep">|</span><span>Owners</span><span class="sep">|</span><span>FAQs</span>
</div>

<div class="abs brand">GENTLE PALM<br>RESIDENCES</div>

<div class="abs social" aria-label="Social links">
  <i style="background:#3b5a9a"></i><i style="background:#3fb7ea"></i><i style="background:#f0841a"></i><i style="background:#4a4a4a"></i><i style="background:#1c74b3"></i>
</div>

<nav class="abs nav">
  <a style="left:32px">Home</a><span class="sep" style="left:100px"></span>
  <a style="left:121px">About Condominium</a><span class="sep" style="left:307px"></span>
  <a style="left:325px">About Apartment</a><span class="sep" style="left:481px"></span>
  <a style="left:502px">Contact Us</a>
  <div class="search">Search</div>
  <div class="go">Go</div>
</nav>

<section class="abs hero">
  <div class="hero-photo" role="img" aria-label="Photo of the penthouse living room with wooden floor, glass table and terrace"></div>
  <div class="hero-caption"></div>
</section>
<svg class="abs arrow" style="left:28px" viewBox="0 0 46 46"><path d="M27 16 L20 23 L27 30" fill="none" stroke="#1a7fd0" stroke-width="3"/></svg>
<svg class="abs arrow" style="left:1134px" viewBox="0 0 46 46"><path d="M19 16 L26 23 L19 30" fill="none" stroke="#1a7fd0" stroke-width="3"/></svg>
<div class="abs hero-title">Duplex Penthouse 4 suites</div>
<div class="abs hero-text">This is the landing page and should make it obvious that there is an apartment for sale in Barra Da Tijuca, Rio De Janeiro with the following attributes</div>
<div class="abs hero-price">Price R$ 2.200.000</div>
<div class="abs read-more">Read more</div>

<h2 class="abs heading" style="left:48px;top:598px">Welcome To <b>Gentle Palm Residences</b></h2>
<div class="abs underline" style="left:44px;top:634px;width:421px"></div>
<div class="abs welcome-box">
  There are many variations of passages of Lorem Ipsum available, but the majority have suffered alteration in some form, by injected humour, or randomised words which don't look even slightly believable. If you are going to use a passage of Lorem Ipsum<br>
  <span class="more">Read More</span>
</div>

<h2 class="abs heading" style="left:48px;top:770px">About <b>Condominium</b></h2>
<div class="abs photo" style="left:45px;top:815px;width:356px;height:149px;background:linear-gradient(180deg,#2f3a44 0%,#5b6670 45%,#8a5b45 70%,#2fa9d8 100%)" role="img" aria-label="Photo of the condominium pool deck with sun loungers"></div>

<h2 class="abs heading" style="left:425px;top:770px">About <b>Apartment</b></h2>
<div class="abs photo" style="left:425px;top:815px;width:356px;height:149px;background:linear-gradient(180deg,#c9d7e4 0%,#a9a59c 45%,#7f8a72 70%,#b7b1a6 100%)" role="img" aria-label="Photo of the building entrance and driveway"></div>

<h2 class="abs heading small" style="left:805px;top:602px">Apartment <b>Features</b></h2>
<div class="abs underline" style="left:805px;top:634px;width:176px"></div>
<div class="abs features">
  <div class="feature" style="top:13px">
    <div class="thumb"><div style="background:linear-gradient(180deg,#8fa9c2,#7a8a86 50%,#4f8fa8)" role="img" aria-label="Photo of the beachfront skyline"></div></div>
    <div class="f-title">Lorem Ipsum</div>
    <div class="f-addr">Seaward, CA 90410</div>
    <div class="f-price">$424,000</div>
    <div class="f-specs">3 Bed, 2 Bath, 2,322 Sq Ft</div>
  </div>
  <div class="feature" style="top:118px">
    <div class="thumb"><div style="background:linear-gradient(180deg,#9fb3c6,#7d6a52 55%,#4a3526)" role="img" aria-label="Photo of the terrace view over the hills"></div></div>
    <div class="f-title">Lorem Ipsum</div>
    <div class="f-addr">Seaward, CA 90410</div>
    <div class="f-price">$1,278,000</div>
    <div class="f-specs">5 Bed, 4 Bath, 5,563 Sq Ft</div>
  </div>
  <div class="feature" style="top:224px">
    <div class="thumb"><div style="background:linear-gradient(180deg,#e4e6e8,#b9b4ab 55%,#6d5a48)" role="img" aria-label="Photo of the bright apartment interior"></div></div>
    <div class="f-title">Lorem Ipsum</div>
    <div class="f-addr">Seaward, CA 90410</div>
    <div class="f-price">$235,000</div>
    <div class="f-specs">1 Bed, 1 Bath, 776 Sq Ft</div>
  </div>
</div>

<footer class="abs footer">
  <div class="footer-links">Home &nbsp;| &nbsp;About Us &nbsp;| &nbsp;Blog &nbsp;| &nbsp;Press &amp; Media &nbsp;| &nbsp;Contact Us &nbsp;| &nbsp;FAQs &nbsp;| &nbsp;Booking terms &nbsp;| &nbsp;Site map &nbsp;| &nbsp;Terms of use &nbsp;| &nbsp;Privacy</div>
  <div class="copyright">© Gentle Palm Residences 2013</div>
</footer>
</body>
</html>
```